Event Poster - Tarawera Mist Fest 2018 (Need ASAP)

Create a poster for an upcoming vape event, located in Waikato, Hamilton, New Zealand.

Mist Fest is an event where lots of shops come to a location, and the public are welcomed and they all vape, buy vape products, socialize, drink beer and have fun.

VISIT THE EVENT WEBSITE FOR INFO - www.taraweramistfest.co.nz

We have created a website at, as you can see the logo and design is a bit boring and plain, so we dont really want it to look anything like that, The logo that is created to suit the poster will be able to be

Need a poster done up so we can send it around, post it up on boards, share on social media etc

I have attached previous events from nearby towns, for reference, but I want something much better.

Target Market(s)

25-45 Male / Female

Requirements
Must have
• - Tarawera Mist Fest 2018
• - Saturday, 2nd June 2018
• - 12-10pm
• - R18 Event (important for public to know)
• - Vendors, Prizes, Comps, Cloud Liquid Medals, Entertainment, Giveaways & More
• - The Corner Alehouse (14 Moller Ln, Kopuku, Hamilton)
• - mention something along lines "Join Tarawera's Opening Mist Fest"
• - "Grab Your Passes at www.taraweramistfest.co.nz NOW"
• - I want people to know they can buy it from a store as well "The Haze Hut"
Nice to have
• Our City colors are Red,Yellow,Black which is symbolic for "Waikato" so it would be nice to have those integrated in there. Alot of the other Mist Fest events have dark, bogan, amateur look done to them, so I want ours to be just a much better version.
• To Clarify, Hamilton is a city inside the Waikato
• I might want to put sponsors on there as well, possibly 10-20, but maybe only a few if space is a problem

```html
<!DOCTYPE html>
<html lang="en">
<head>
<meta charset="utf-8">
<title>Tarawera Mist Fest 2018 – Event Poster</title>
<link href="https://fonts.googleapis.com/css2?family=Archivo+Black&family=Bebas+Neue&display=swap" rel="stylesheet">
<style>
  :root {
    --black: #050505;
    --red: #e31e24;
    --yellow: #fff200;
    --white: #ffffff;
    --smoke: #8a8a8a;
    --stage: #e9e9e9;
  }
  html, body {
    margin: 0;
    width: 1200px;
    height: 704px;
    overflow: hidden;
    background: var(--stage);
  }
  .stage {
    position: relative;
    width: 1200px;
    height: 704px;
  }
  .poster-frame {
    position: absolute;
    left: 350px;
    top: 0;
    width: 499px;
    height: 704px;
    overflow: hidden;
  }
  .poster {
    position: absolute;
    left: 0;
    top: 0;
    width: 582px;
    height: 821px;
    transform: scale(0.8575);
    transform-origin: 0 0;
    background: var(--black);
    font-family: "Bebas Neue", "Arial Narrow", sans-serif;
    color: var(--white);
  }
  .hero-photo {
    position: absolute;
    left: 0;
    top: 0;
    width: 582px;
    height: 450px;
    background:
      radial-gradient(ellipse 90px 150px at 455px 140px, #d9d9d9 0%, #bdbdbd 60%, rgba(189,189,189,0) 100%),
      radial-gradient(ellipse 300px 150px at 300px 340px, rgba(150,150,150,0.55) 0%, rgba(40,40,40,0) 100%),
      radial-gradient(ellipse 220px 160px at 200px 120px, rgba(120,120,120,0.45) 0%, rgba(20,20,20,0) 100%),
      var(--black);
  }
  .pill {
    position: absolute;
    display: flex;
    align-items: center;
    justify-content: center;
    box-sizing: border-box;
  }
  .title-top {
    left: 0; top: 80px; width: 318px; height: 60px;
    background: var(--red);
    border: 3px solid var(--yellow);
    border-left: none;
    border-radius: 0 30px 30px 0;
    font-family: "Archivo Black", sans-serif;
    font-size: 44px;
    letter-spacing: 1px;
    text-shadow: 3px 3px 0 rgba(0,0,0,0.6);
  }
  .title-main {
    position: absolute;
    left: 22px; top: 136px;
    margin: 0;
    font-weight: 400;
    font-size: 150px;
    line-height: 1;
    color: var(--yellow);
    letter-spacing: 1px;
    text-shadow: 4px 4px 0 rgba(0,0,0,0.7);
    white-space: nowrap;
  }
  .title-year {
    left: 0; top: 272px; width: 300px; height: 84px;
    background: var(--red);
    border: 3px solid var(--yellow);
    border-left: none;
    border-radius: 0 42px 42px 0;
    font-family: "Archivo Black", sans-serif;
    font-size: 72px;
    text-shadow: 4px 4px 0 rgba(0,0,0,0.6);
  }
  .date-burst {
    position: absolute;
    left: 412px; top: 282px;
    width: 164px; height: 164px;
  }
  .date-burst-text {
    position: absolute;
    inset: 0;
    display: flex;
    align-items: center;
    justify-content: center;
    text-align: center;
    font-size: 31px;
    line-height: 0.95;
    color: var(--red);
    transform: rotate(-14deg);
  }
  .info-tag {
    top: 463px; height: 46px;
    background: var(--yellow);
    color: var(--black);
    font-size: 38px;
    padding-top: 3px;
  }
  .info-time { left: 0; width: 200px; border-radius: 0 23px 23px 0; }
  .info-age { left: 333px; width: 249px; border-radius: 23px 0 0 23px; }
  .features {
    position: absolute;
    left: 0; top: 518px; width: 582px;
    margin: 0;
    text-align: center;
    font-size: 36px;
    line-height: 36px;
  }
  .venue-band {
    left: 0; top: 603px; width: 582px; height: 38px;
    background: var(--red);
    font-size: 29px;
    padding-top: 3px;
  }
  .tagline {
    position: absolute;
    left: 0; top: 650px; width: 582px;
    margin: 0;
    text-align: center;
    font-size: 45px;
    line-height: 50px;
    color: var(--yellow);
    white-space: nowrap;
  }
  .tickets {
    position: absolute;
    left: 0; top: 704px; width: 582px;
    margin: 0;
    text-align: center;
    font-size: 19px;
    line-height: 22px;
  }
  .tickets .url { color: var(--yellow); }
  .store-band {
    position: absolute;
    left: 0; top: 757px; width: 582px; height: 64px;
    background: var(--red);
  }
  .store-note {
    position: absolute;
    left: 16px; top: 18px;
    margin: 0;
    font-size: 30px;
    line-height: 32px;
  }
  .store-name {
    position: absolute;
    left: 396px; top: 16px;
    display: flex;
    align-items: center;
    gap: 10px;
    font-size: 34px;
    line-height: 34px;
    color: var(--white);
    padding-top: 2px;
  }
  .store-mark {
    width: 14px; height: 14px;
    background: var(--yellow);
    margin-top: -4px;
  }
</style>
</head>
<body>
<main class="stage">
  <div class="poster-frame">
    <article class="poster">
      <div class="hero-photo" role="img" aria-label="Photo of a white box-mod vaporiser with billowing vapour clouds on a black background"></div>

      <div class="pill title-top">TARAWERA</div>
      <h1 class="title-main">MIST FEST</h1>
      <div class="pill title-year">2018</div>

      <div class="date-burst">
        <svg width="164" height="164" viewBox="0 0 164 164" aria-hidden="true">
          <polygon fill="#fff200" points="82,0 90,22 103,3 106,27 122,11 119,35 139,24 131,47 153,41 141,61 164,62 146,75 164,86 145,94 158,113 135,113 143,134 121,127 122,150 102,137 96,160 82,142 68,160 62,137 42,150 43,127 21,134 29,113 6,113 19,94 0,86 18,75 0,62 23,61 11,41 33,47 25,24 45,35 42,11 58,27 61,3 74,22"/>
        </svg>
        <div class="date-burst-text">SATURDAY,<br>2ND JUNE<br>2018</div>
      </div>

      <div class="pill info-tag info-time">12-10PM</div>
      <div class="pill info-tag info-age">R18 EVENT</div>

      <p class="features">VENDORS, PRIZES, COMPS, CLOUD LIQUID MEDALS,<br>ENTERTAINMENT, GIVEAWAYS &amp; MORE</p>

      <div class="pill venue-band">THE CORNER ALEHOUSE (14 MOLLER LN, KOPUKU, HAMILTON)</div>

      <p class="tagline">" JOIN TARAWERA'S OPENING MIST FEST "</p>
      <p class="tickets">"GRAB YOUR PASSES AT <span class="url">WWW.TARAWERAMISTFEST.CO.NZ</span> NOW"</p>

      <footer class="store-band">
        <p class="store-note">YOU CAN BUY VAPE FROM A STORE AS WELL</p>
        <div class="store-name"><span class="store-mark"></span>THE HAZE HUT</div>
      </footer>
    </article>
  </div>
</main>
</body>
</html>
```